Marquen Premium Men's Shaving Cream Product Label . Cream packaged in a Amber Jar/Black Top Cap.

Please include information ( see Marquen design Template attachment) designed on a Round Top cap. Label Diameter: 3.125" NOTE: Design this First,
Wrap Around Label: 11.3125 x 0.875" (w x h): NOTE: Required latter after selection of Final Design Selection.
Shave Cream packaged in an 8oz Low Profile Amber Jar/Black Top Cap.
Thanks

Target Market(s)

Prime Target-Men Ages 20yrs-65yrs+ and Women 20yrs-65yrs+( they purchase ovr 55% of these Mens care products for partner/spouse/friend.

Industry/Entity Type

Personel Care/Cosmetics/NaturalHealthcare

Other font styles liked:
• At this stage if you would like to submi a desigh that would include both a Top Label and your Wrap-around label on a Amber jar/black top lid. It would be helpful to see how it would look complete. Thanks . Please refer to the updated design Graphic Template for copy and layout . Questions? Let me know. Thanks.Please now use QUILLSTONE on label designs. Thanks! Please see image attachment for added Tree Image Vector that can be added to your design instead of the Original Tree Image .

Requirements
Must have
• Look and Feel of a Quality/Premium Mens Skincare Brand with a Masculine feel but attractive to women as well ( not Macho!).Think Unisex with a Male slant.
Nice to have
• Premium/Quality/Natural Skincare & Bodycare Brand
Should not have
• Not Macho. No Cartoony or Barber Tools/Bearded Men Images. Too gimicky and over-hyped!

```html
<!DOCTYPE html>
<html lang="en">
<head>
<meta charset="utf-8">
<title>Marquen Quillstone Shaving Cream Labels</title>
<link rel="stylesheet" href="https://fonts.googleapis.com/css2?family=Cinzel:wght@400;600;700&display=swap">
<style>
  :root {
    --page: #ffffff;
    --label-dark: #262626;
    --label-deep: #1a1a1a;
    --ring-black: #0d0d0d;
    --white: #ffffff;
    --bronze: #8a6440;
    --silver-edge: #8e8e8e;
    --silver-mid: #d6d6d6;
    --silver-light: #f4f4f4;
    --tree-core: #6b4a2c;
    --tree-bg: #1c1712;
  }
  * { margin: 0; padding: 0; box-sizing: border-box; }
  html, body { width: 1200px; height: 900px; overflow: hidden; background: var(--page); }
  .canvas {
    position: relative;
    width: 1200px;
    height: 900px;
    background: var(--page);
    font-family: "Cinzel", serif;
  }

  /* Wrap-around label, flat */
  .wrap-label {
    position: absolute;
    left: 216px;
    top: 412px;
    width: 489px;
    height: 214px;
    background: linear-gradient(180deg, var(--label-dark), var(--label-deep));
    color: var(--white);
    text-align: center;
  }
  .wrap-label .brand {
    position: absolute;
    left: 0; right: 0;
    top: 38px;
    font-size: 17px;
    font-weight: 700;
    letter-spacing: 3px;
    line-height: 1;
  }
  .wrap-label .brand-rule {
    position: absolute;
    left: 196px; width: 98px;
    top: 60px;
    height: 1px;
    background: var(--white);
  }
  .wrap-label .emblem {
    position: absolute;
    left: 216px;
    top: 66px;
    width: 56px;
    height: 56px;
    border-radius: 50%;
    border: 1px solid var(--bronze);
    background: radial-gradient(circle, var(--tree-core) 0%, var(--tree-bg) 70%);
  }
  .wrap-label .silver-band {
    position: absolute;
    left: 0; right: 0;
    top: 117px;
    height: 35px;
    background: linear-gradient(90deg, var(--silver-edge), var(--silver-light) 35%, var(--silver-mid) 70%, var(--silver-edge));
  }
  .wrap-label .product {
    position: absolute;
    left: 0; right: 0;
    top: 116px;
    font-size: 20px;
    color: var(--bronze);
    line-height: 20px;
    letter-spacing: 0.5px;
  }
  .wrap-label .product-type {
    position: absolute;
    left: 0; right: 0;
    top: 136px;
    font-size: 13px;
    color: var(--bronze);
    line-height: 14px;
    letter-spacing: 1px;
  }
  .wrap-label .french {
    position: absolute;
    left: 0; right: 0;
    top: 159px;
    font-size: 11px;
    line-height: 12px;
    letter-spacing: 0.5px;
  }
  .wrap-label .details {
    position: absolute;
    left: 0; right: 0;
    top: 174px;
    font-size: 7px;
    line-height: 10px;
    letter-spacing: 0.5px;
  }

  /* Round top label, flat */
  .top-label {
    position: absolute;
    left: 738px;
    top: 318px;
    width: 308px;
    height: 308px;
  }
  .top-label text { font-family: "Cinzel", serif; }
</style>
</head>
<body>
<main class="canvas">

  <section class="wrap-label" aria-label="Wrap-around jar label">
    <div class="brand">MARQUEN</div>
    <div class="brand-rule"></div>
    <div class="emblem" role="img" aria-label="Circular tree-of-life emblem in bronze"></div>
    <div class="silver-band"></div>
    <div class="product">QUILLSTONE</div>
    <div class="product-type">SHAVING CREAM</div>
    <div class="french">CRÈME DE RASAGE</div>
    <div class="details">FERNHOLLOW ABSOLU<br>1935<br>150G e 5.3 OZ</div>
  </section>

  <svg class="top-label" viewBox="0 0 308 308" aria-label="Round lid label">
    <defs>
      <linearGradient id="silver-band-fill" x1="0" x2="1" y1="0" y2="0">
        <stop offset="0" stop-color="#8e8e8e"/>
        <stop offset="0.35" stop-color="#f4f4f4"/>
        <stop offset="0.7" stop-color="#d6d6d6"/>
        <stop offset="1" stop-color="#8e8e8e"/>
      </linearGradient>
      <radialGradient id="emblem-fill">
        <stop offset="0" stop-color="#6b4a2c"/>
        <stop offset="0.7" stop-color="#1c1712"/>
      </radialGradient>
      <clipPath id="inner-disc"><circle cx="154" cy="154" r="128"/></clipPath>
    </defs>
    <circle class="outer-ring" cx="154" cy="154" r="154" fill="#0d0d0d"/>
    <circle class="frame-ring" cx="154" cy="154" r="137" fill="none" stroke="#ffffff" stroke-width="3"/>
    <circle class="frame-line" cx="154" cy="154" r="131" fill="none" stroke="#ffffff" stroke-width="1.5"/>
    <circle class="inner-field" cx="154" cy="154" r="129" fill="#222222"/>
    <text x="154" y="87" text-anchor="middle" fill="#ffffff" font-size="20" font-weight="700" letter-spacing="3">MARQUEN</text>
    <line x1="98" y1="94" x2="210" y2="94" stroke="#ffffff" stroke-width="1"/>
    <rect x="0" y="102" width="308" height="54" fill="url(#silver-band-fill)" clip-path="url(#inner-disc)"/>
    <text x="154" y="127" text-anchor="middle" fill="#8a6440" font-size="19" letter-spacing="0.5">QUILLSTONE</text>
    <text x="154" y="148" text-anchor="middle" fill="#8a6440" font-size="12.5" letter-spacing="1">SHAVING CREAM</text>
    <text x="154" y="170" text-anchor="middle" fill="#ffffff" font-size="9.5" letter-spacing="0.5">CRÈME DE RASAGE</text>
    <circle cx="154" cy="208" r="33" fill="url(#emblem-fill)" stroke="#8a6440" stroke-width="1" role="img" aria-label="Circular tree-of-life emblem in bronze"/>
    <text x="154" y="254" text-anchor="middle" fill="#ffffff" font-size="9" letter-spacing="0.5">FERNHOLLOW ABSOLU</text>
    <text x="154" y="266" text-anchor="middle" fill="#ffffff" font-size="9">1935</text>
    <text x="154" y="277" text-anchor="middle" fill="#ffffff" font-size="7">150G e 5.3 OZ</text>
  </svg>

</main>
</body>
</html>
```